Higher $ Now Guaranteed! Redesign Web Page(s) Style Composition and Color (Graphics design-not code)

We need a modern look for an existing website. You can either use or change the current logo. Choice of colors, fonts, style is up to you. Sample URLs and additional details are provided in the attached document. Most of our struggle has been the appearance of the directory listings (city) page.
----------------------------------------------------------------------------------
--> Increased Project Budget and Now Funds are GUARANTEED
--> Added an additional attachment in response to questions
-->THIS PROJECT IS FOR GRAPHICS/DESIGN NOT CODE
The project is mostly a few areas of text and colored boxes or lines. Hopefully a skilled designer can place these elements in an attractive layout and choose the right colors and styles. There are no complex drawings required for this project.

*** We are involved with other projects from time to time and expect that the winning designer will be given the first opportunity at this future work. ***

*** There is no requirement to do any code but if you submit a design feel free to indicate if you wish to be considered for any future code work on this site or others ***

Font styles to use
Sans Serif

Requirements
Must have
• Rounded corners on images and buttons with nice gradients or hover effects.
Nice to have
• Attached an additional descriptions document to help with these answers.
Should not have
• Small fonts, traditional older looking rectangular buttons, dull or boring color schemes

```html
<!DOCTYPE html>
<html lang="en">
<head>
<meta charset="utf-8">
<title>LocalTaxPros – Find the Best Tax Professionals</title>
<link rel="stylesheet" href="https://fonts.googleapis.com/css2?family=Raleway:wght@400;500;600;700&display=swap">
<style>
:root{
  --ink:#1b1b1b;
  --navy:#17262e;
  --muted:#6f7478;
  --green-top:#8cc63f;
  --green-bot:#5ea52a;
  --orange-top:#f5a033;
  --orange-bot:#e0761b;
  --blue:#1aa0de;
  --purple-top:#b879c2;
  --purple-bot:#8e4f99;
  --line-orange:#f0932b;
  --line-magenta:#c8246e;
  --line-purple:#6e2c80;
  --line-yellow:#f4d23a;
  --line-green:#8cc63f;
  --line-blue:#2aa4e0;
  --field:#b9bec2;
}
*{box-sizing:border-box;margin:0;padding:0}
html,body{width:1200px;height:773px;overflow:hidden;background:#fff}
body{position:relative;font-family:"Raleway",Arial,sans-serif;color:var(--ink)}
.site-header{position:absolute;left:0;top:0;width:1200px;height:66px;background:#fff}
.brand{position:absolute;left:240px;top:20px;display:flex;align-items:center;gap:6px;font-size:19px;font-weight:700;color:var(--navy)}
.brand-dot{width:10px;height:10px;border-radius:50%;background:var(--navy)}
.main-nav{position:absolute;left:520px;top:38px;display:flex;font-size:12px;font-weight:500}
.main-nav a{color:var(--ink);text-decoration:none;padding:0 12px;border-left:1px solid #999;line-height:14px}
.main-nav a:first-child{border-left:0}
.phone{position:absolute;left:848px;top:36px;display:flex;align-items:center;gap:4px;font-size:15px;font-weight:600}
.rainbow{position:absolute;left:0;width:1200px;height:3px;background:linear-gradient(90deg,var(--line-orange) 0 20%,var(--line-magenta) 20% 28%,var(--line-purple) 28% 38.5%,var(--line-yellow) 38.5% 50%,var(--line-green) 50% 59.5%,var(--line-blue) 59.5% 100%)}
.hero-bg{position:absolute;left:0;top:68px;width:1200px;height:542px;background:radial-gradient(ellipse at 22% 30%,#cfd4d8 0,#e9ecee 35%,transparent 60%),linear-gradient(180deg,#f3f4f5,#e6e9ec 60%,#dfe3e6)}
.hero-title{position:absolute;left:0;top:96px;width:1200px;text-align:center;font-size:18px;font-weight:700;letter-spacing:.2px}
.hero-sub{position:absolute;left:0;top:121px;width:1200px;text-align:center;font-size:11px;font-weight:500}
.search-card{position:absolute;left:271px;top:165px;width:167px;height:215px;background:#fff;border-radius:3px;box-shadow:0 2px 6px rgba(0,0,0,.08);overflow:hidden}
.search-head{height:51px;background:linear-gradient(var(--green-top),var(--green-bot));color:#fff;text-align:center;font-size:14px;font-weight:500;line-height:17px;padding-top:8px}
.field{position:absolute;left:13px;width:141px;height:22px;border:1px solid var(--field);font-size:9px;color:#888;padding:5px 4px;border-radius:2px}
.field svg{position:absolute;right:5px;top:7px}
.or{position:absolute;left:0;width:167px;top:130px;text-align:center;font-size:9px}
.search-btn{position:absolute;left:13px;top:182px;width:141px;height:22px;border-radius:3px;background:linear-gradient(var(--orange-top),var(--orange-bot));color:#fff;font-size:11px;font-weight:600;text-align:center;line-height:22px}
.map{position:absolute;left:575px;top:166px;width:355px;height:220px;background:linear-gradient(135deg,#1f3038,#17262e);border-radius:14px 30px 20px 40px}
.about-band{position:absolute;left:0;top:427px;width:1200px;height:28px;background:var(--navy);color:#fff;font-size:14px;font-weight:600;text-align:center;line-height:28px}
.about-body{position:absolute;left:0;top:455px;width:1200px;height:155px;background:rgba(255,255,255,.88)}
.about-text{position:absolute;left:271px;top:485px;width:440px;font-size:8px;line-height:10.2px}
.about-text p+p{margin-top:10px}
.promo{position:absolute;left:762px;top:486px;width:167px;height:94px;background:var(--blue);text-align:center;color:var(--navy)}
.promo h3{font-size:8px;font-weight:700;margin-top:12px}
.promo p{font-size:6px;line-height:7.5px;margin:11px 12px 0}
.promo-btn{display:block;margin:7px auto 0;width:140px;height:20px;border-radius:3px;background:linear-gradient(var(--purple-top),var(--purple-bot));color:#fff;font-size:11px;font-weight:600;line-height:20px}
.site-footer{position:absolute;left:0;top:613px;width:1200px;height:122px;background:var(--navy);color:#d4d8db}
.foot-col{position:absolute;top:26px;font-size:11px;line-height:15px}
.foot-col h4{font-size:11px;font-weight:600;margin-bottom:15px;letter-spacing:.3px}
.divider{position:absolute;top:9px;width:1px;height:104px;background:#7d8a91}
.foot-brand{position:absolute;left:860px;top:50px;font-size:16px;font-weight:700;color:#4b5a62;display:flex;align-items:center;gap:5px}
.foot-brand span{width:8px;height:8px;border-radius:50%;background:#4b5a62}
.copyright{position:absolute;left:0;top:748px;width:1200px;text-align:center;font-size:10px;color:var(--muted)}
</style>
</head>
<body>
<header class="site-header">
  <div class="brand"><span class="brand-dot"></span>LocalTaxPros</div>
  <nav class="main-nav"><a href="#">Home</a><a href="#">Get Listed</a><a href="#">Contact Us</a><a href="#">Members Login</a></nav>
  <div class="phone"><svg width="12" height="13" viewBox="0 0 24 24"><path fill="#1b1b1b" d="M6.6 10.8a15.1 15.1 0 006.6 6.6l2.2-2.2c.3-.3.7-.4 1-.2 1.1.4 2.3.6 3.6.6.6 0 1 .4 1 1V20c0 .6-.4 1-1 1A17 17 0 013 4c0-.6.4-1 1-1h3.5c.6 0 1 .4 1 1 0 1.3.2 2.5.6 3.6.1.3 0 .7-.2 1z"/></svg>555-204-7719</div>
</header>
<div class="rainbow" style="top:66px"></div>

<div class="hero-bg" role="img" aria-label="Soft blurred photo of a magnifying glass over tax forms"></div>
<h1 class="hero-title">FIND THE BEST TAX PROFESSIONALS IN YOUR AREA</h1>
<p class="hero-sub">Our directories of tax professionals give you immediate access to the very best tax preparers and income tax advisors in your area.</p>

<form class="search-card">
  <div class="search-head">FIND TAX &nbsp;EXPERTS<br>NEAR YOU</div>
  <div class="field" style="top:63px">State<svg width="12" height="6"><path d="M0 0l6 6 6-6" fill="none" stroke="#aaa"/></svg></div>
  <div class="field" style="top:97px">City<svg width="12" height="6"><path d="M0 0l6 6 6-6" fill="none" stroke="#aaa"/></svg></div>
  <div class="or">OR</div>
  <div class="field" style="top:147px">Zip Code</div>
  <div class="search-btn">SEARCH</div>
</form>

<div class="map" role="img" aria-label="Clickable map of the United States with state labels"></div>

<div class="about-body"></div>
<h2 class="about-band">About LOCALTAXPROS.COM</h2>
<div class="about-text">
  <p>Lorem ipsum dolor sit amet, consectetur adipiscing elit. Morbi pulvinar at mi eu hendrerit. Sed sagittis turpis lacus, ac ultrices diam ullamcorper nec. Nulla facilisi. Sed in blandit ligula, eu laoreet ex. Ut eleifend mi eget vulputate ultricies. Suspendisse nec nibh non ligula suscipit malesuada. Mauris a urna id arcu sollicitudin laoreet.</p>
  <p>Donec rutrum velit enim, a sollicitudin nisi tempus vitae. Lorem ipsum dolor sit amet, consectetur adipiscing elit. Fusce ultrices tempus pellentesque. Sed congue euismod urna a dignissim. Cras quis metus nec tortor pretium vehicula. Sed vel convallis enim, id luctus dolor. Quisque dui quam, sollicitudin ut neque vitae, fringilla luctus magna.</p>
</div>
<aside class="promo">
  <h3>ARE YOU TAX PREPARER ?</h3>
  <p>Our directories of tax professionals give you immediate access to the very best tax preparers and income tax advisors in your area.</p>
  <span class="promo-btn">GET LISTED</span>
</aside>

<div class="rainbow" style="top:610px"></div>
<footer class="site-footer">
  <div class="foot-col" style="left:240px"><h4>NAVIGATION</h4>Directory<br>Special Offers<br>Contact Us</div>
  <div class="divider" style="left:375px"></div>
  <div class="foot-col" style="left:441px"><h4>CONTACT</h4>PO Box 4410<br>Millbrook, CT<br>06099</div>
  <div class="divider" style="left:565px"></div>
  <div class="foot-col" style="left:634px"><h4>LEGAL</h4></div>
  <div class="foot-brand"><span></span>LocalTaxPros</div>
</footer>
<p class="copyright">www.localtaxpros.com © All Rights Reserved.</p>
</body>
</html>
```